Change of trading name, rebrand

existing website to be updated with new theme and logo. existing website is
www.brackenridgeworks.com.au
Industry/Entity Type
Construction
Coding
Coded - Design and coding required
Number of Pages Required
5+ page
Requirements
Must have
- be mobile phone friendly

```html
<!DOCTYPE html>
<html lang="en">
<head>
<meta charset="utf-8">
<meta name="viewport" content="width=device-width, initial-scale=1">
<title>BRW Heavy Equipment Hire</title>
<link href="https://fonts.googleapis.com/css2?family=Poppins:ital,wght@0,300;0,400;0,500;0,600;0,700;1,500&display=swap" rel="stylesheet">
<style>
:root{
  --ink:#141414;
  --dark:#1c1c1e;
  --navy:#232a7a;
  --navy-deep:#1b2163;
  --accent:#5b63ea;
  --grey:#6f6f74;
  --light:#eef0f7;
  --lav:#c9cce6;
  --white:#ffffff;
  --line:#e3e4ea;
}
*{box-sizing:border-box;margin:0;padding:0}
html,body{width:1200px;height:3846px;overflow:hidden}
body{font-family:"Poppins",sans-serif;color:var(--ink);background:var(--white);position:relative}
.abs{position:absolute}
a{color:inherit;text-decoration:none}

/* hero */
.hero{position:absolute;left:0;top:0;width:1200px;height:748px;background:var(--ink);overflow:hidden}
.hero-photo{position:absolute;left:0;top:0;width:1200px;height:748px;
  clip-path:polygon(1040px 0,1200px 0,1200px 748px,470px 748px);
  background:radial-gradient(ellipse at 75% 45%,#d19a2a 0%,#8a6a32 28%,#6b6458 52%,#3d3e42 80%)}
.logo-box{position:absolute;left:93px;top:0;width:114px;height:78px;background:var(--white);border-radius:0 0 6px 6px;display:flex;align-items:center;justify-content:center;flex-direction:column}
.logo-name{font-weight:700;font-size:24px;color:var(--navy);letter-spacing:1px;line-height:1}
.logo-sub{font-weight:600;font-size:7px;color:var(--ink);letter-spacing:2px;margin-top:3px}
.nav{position:absolute;top:36px;left:340px;display:flex;gap:28px;font-size:11px;color:var(--white);font-weight:400}
.nav .phone{color:var(--accent);display:flex;gap:8px;align-items:center;margin-left:4px}
.eyebrow{font-size:10px;letter-spacing:3px;color:#c9c9cf;text-transform:uppercase}
.hero h1{position:absolute;left:93px;top:185px;font-size:58px;line-height:64px;font-weight:700;color:var(--white);text-transform:uppercase}
.hero p{position:absolute;left:93px;top:323px;width:335px;font-size:10.5px;line-height:18.8px;color:#e5e5e8}
.btn{display:inline-flex;align-items:center;justify-content:center;background:var(--navy);color:var(--white);font-weight:600;font-size:12.5px;text-transform:uppercase;box-shadow:0 10px 26px rgba(60,70,220,.45)}

/* features */
.features{position:absolute;left:93px;top:638px;width:1012px;height:244px;background:var(--white);box-shadow:0 10px 40px rgba(0,0,0,.08)}
.feat{position:absolute;top:0;width:230px;text-align:center;padding-top:32px}
.feat h3{font-size:14px;font-weight:600;margin:14px 0 10px}
.feat p{font-size:10px;line-height:17.5px;color:#55555b;padding:0 22px}
.feat-dark{position:absolute;left:581px;top:608px;width:266px;height:305px;background:var(--ink);color:var(--white);text-align:center;padding-top:52px;box-shadow:0 16px 36px rgba(0,0,0,.28)}
.feat-dark h3{font-size:14px;font-weight:600;margin:14px 0 10px}
.feat-dark p{font-size:10px;line-height:17.5px;color:#e8e8ea;padding:0 52px}

/* about */
.about-bg{position:absolute;left:0;top:1000px;width:1200px;height:591px;background:linear-gradient(180deg,#fff 0%,#f3f4fa 100%);clip-path:polygon(0 260px,0 100%,100% 100%,100% 0,460px 591px)}
.about-bg2{position:absolute;left:0;top:1000px;width:1200px;height:591px;background:linear-gradient(200deg,#dfe1f1,#f6f7fb);clip-path:polygon(1200px 190px,1200px 591px,460px 591px)}
.photo-back{left:103px;top:1026px;width:402px;height:341px;background:linear-gradient(160deg,#59663f,#8a8f74 55%,#6b5a40)}
.photo-front{left:179px;top:1110px;width:451px;height:368px;background:linear-gradient(180deg,#4d8fd6 0%,#9ec4ec 40%,#c57a46 70%,#a5552b 100%);box-shadow:0 20px 40px rgba(0,0,0,.2)}
.about-text{left:722px;top:1064px;width:350px}
.h2{font-size:31px;line-height:34px;font-weight:700;text-transform:uppercase;color:var(--ink)}
.about-text p{font-size:10.3px;line-height:18.9px;color:#4e4e54;margin-top:20px}

/* stats */
.stats{position:absolute;left:0;top:1591px;width:1200px;height:339px;background:linear-gradient(180deg,#262628,#1a1a1c);color:var(--white)}
.stat{position:absolute;top:95px;width:200px;text-align:center}
.stat .num{font-size:34px;font-weight:700;line-height:40px;margin-top:10px}
.stat .lbl{font-size:14px;font-weight:300;line-height:19px;color:#ececee}
.stat .lbl.only{margin-top:26px}

/* plant hire */
.plant{position:absolute;left:0;top:1930px;width:1200px;height:640px;background:var(--white);overflow:hidden}
.plant-deco{position:absolute;right:0;top:0;width:250px;height:560px;background:linear-gradient(200deg,#c6c9e4,#eef0f8);clip-path:polygon(100% 0,100% 100%,60% 100%,0 300px,170px 0)}
.center{text-align:center;width:1200px;left:0}
.arrow{position:absolute;top:367px;width:40px;height:40px;border-radius:50%;background:var(--ink);display:flex;align-items:center;justify-content:center}

/* partners */
.partner{position:absolute;top:2584px;height:50px;background:#c9c9cc;border-radius:4px;opacity:.75}

/* contact */
.contact-photo{left:0;top:2690px;width:745px;height:700px;background:linear-gradient(180deg,#fff 0%,#b9d2ee 18%,#8fb6e2 40%,#d2a248 62%,#b49a77 82%,#c9bfae 100%);
  -webkit-mask-image:linear-gradient(90deg,#000 80%,transparent 100%);mask-image:linear-gradient(90deg,#000 80%,transparent 100%)}
.contact-deco{position:absolute;left:930px;top:2940px;width:270px;height:450px;background:linear-gradient(200deg,#c7cae5,#eceef7);clip-path:polygon(100% 0,100% 100%,0 100%)}
.form{position:absolute;left:671px;top:2873px;width:394px;height:372px;background:var(--white);box-shadow:0 14px 40px rgba(0,0,0,.08);padding:20px 14px}
.form .title{font-size:11px;font-weight:500}
.field{border:1px solid var(--line);height:43px;margin-top:9px;font-size:8.5px;color:#9a9aa0;padding:15px 22px}
.field.big{height:70px}
.strap{left:205px;top:3371px;font-size:22px;font-weight:700;color:rgba(255,255,255,.55);letter-spacing:.5px}
.strap-sub{left:205px;top:3409px;font-size:9.5px;color:#dadade}

/* footer */
.footer h4{font-size:13px;font-weight:600}
.flist{list-style:none;font-size:10px;line-height:18.7px;color:#66666c}
.flist li::before{content:"» ";color:#aaa}
.social{width:24px;height:24px;border-radius:50%;background:#ececee;position:absolute;top:3683px}
.copybar{position:absolute;left:0;top:3808px;width:1200px;height:38px;background:#ececee;font-size:9px;color:#555}
</style>
</head>
<body>

<section class="hero">
  <div class="hero-photo" role="img" aria-label="Yellow track dozer with muddy blade on a dirt site"></div>
  <div class="logo-box"><span class="logo-name">BRW</span><span class="logo-sub">PLANT HIRE</span></div>
  <nav class="nav">
    <a>Home</a><a>About Us</a><a>Plant Hire ⌄</a><a>Major Project Snapshot ⌄</a><a>Policies</a><a>Jobs</a><a>Contact Us</a>
    <a class="phone"><svg width="11" height="11" viewBox="0 0 24 24"><path fill="#5b63ea" d="M6.6 10.8a15 15 0 006.6 6.6l2.2-2.2c.3-.3.7-.4 1-.2 1.1.4 2.3.6 3.6.6.6 0 1 .4 1 1V20c0 .6-.4 1-1 1A17 17 0 013 4c0-.6.4-1 1-1h3.5c.6 0 1 .4 1 1 0 1.3.2 2.5.6 3.6.1.3 0 .7-.2 1z"/></svg>1300 462 915</a>
  </nav>
  <div class="abs eyebrow" style="left:93px;top:157px">Welcome to BRW</div>
  <h1>BRW Heavy<br>Equipment Hire</h1>
  <p>Brackenridge Works Equipment Hire specialise in the hire of heavy earthmoving, mining and construction machines with specialised attachments and tooling. Wet or dry hire, we provide excellent operators and quality machines across all makes and models to guarantee you maximum up time.</p>
  <a class="btn abs" style="left:93px;top:445px;width:230px;height:58px">Get Free Quotation</a>
</section>

<div class="features">
  <div class="feat" style="left:0">
    <svg width="48" height="44" viewBox="0 0 48 44" fill="none" stroke="#444" stroke-width="1.3"><circle cx="24" cy="27" r="11"/><circle cx="24" cy="27" r="6"/><path d="M21 27l2 2 4-4"/><path d="M24 3l2 4 4 .5-3 3 1 4-4-2-4 2 1-4-3-3 4-.5z"/><path d="M10 9l1 2 2 .3-1.5 1.5.4 2-1.9-1-1.9 1 .4-2L7 11.3 9 11z"/><path d="M38 9l1 2 2 .3-1.5 1.5.4 2-1.9-1-1.9 1 .4-2-1.5-1.5 2-.3z"/></svg>
    <h3>Experience</h3>
    <p>BRW's management team is able to learn from unique challenges faced by our clients and share this knowledge.</p>
  </div>
  <div class="abs" style="left:222px;top:86px;width:1px;height:100px;background:var(--line)"></div>
  <div class="feat" style="left:230px">
    <svg width="48" height="44" viewBox="0 0 48 44" fill="none" stroke="#444" stroke-width="1.3"><circle cx="24" cy="27" r="12"/><path d="M19 31v-6h3l3-5c1 0 2 1 1.5 3l-.5 2h4c1 0 1.5 1 1 2l-1.5 4H19z"/><path d="M24 3l2 4 4 .5-3 3 1 4-4-2-4 2 1-4-3-3 4-.5z"/><path d="M12 10l1 2 2 .3-1.5 1.5.4 2-1.9-1-1.9 1 .4-2L9 12.3l2-.3z"/><path d="M36 10l1 2 2 .3-1.5 1.5.4 2-1.9-1-1.9 1 .4-2-1.5-1.5 2-.3z"/></svg>
    <h3>Quality Matters</h3>
    <p>BRW's equipment is regularly updated in order to remain at the forefront of our industry and to continue to provide the highest of safety standards.</p>
  </div>
  <div class="feat" style="left:760px;width:252px">
    <svg width="44" height="44" viewBox="0 0 44 44" fill="none" stroke="#444" stroke-width="1.3"><rect x="14" y="14" width="16" height="16"/><rect x="19" y="19" width="6" height="6"/><path d="M18 14V6M26 14V6M18 30v8M26 30v8M14 18H6M14 26H6M30 18h8M30 26h8"/><circle cx="18" cy="5" r="1.5"/><circle cx="26" cy="5" r="1.5"/><circle cx="5" cy="18" r="1.5"/><circle cx="39" cy="26" r="1.5"/></svg>
    <h3>Technology</h3>
    <p>Technology increases productivity and reduces project costs. BRW recognises the importance technology plays in successfully.</p>
  </div>
</div>
<div class="feat-dark">
  <svg width="48" height="44" viewBox="0 0 48 44" fill="none" stroke="#fff" stroke-width="2.4" stroke-linecap="round"><circle cx="22" cy="24" r="3"/><path d="M16 30a8 8 0 0112-12"/><path d="M11 35a15 15 0 0121-21"/><path d="M29 22a8 8 0 01-5 9"/><path d="M36 20a15 15 0 01-9 15"/></svg>
  <h3>Diverse Range</h3>
  <p>Diverse range of plant and equipment including a range of specialised attachments not commonly available through general hire companies.</p>
</div>

<div class="about-bg"></div>
<div class="about-bg2"></div>
<div class="abs photo-back" role="img" aria-label="Excavator working beside trees on a roadside site"></div>
<div class="abs photo-front" role="img" aria-label="Yellow wheel loader with raised bucket in a red dirt quarry"></div>
<div class="abs about-text">
  <div class="eyebrow" style="color:#8a8a90;margin-bottom:12px">About Us</div>
  <h2 class="h2">Committed to<br>superior quality<br>hire services</h2>
  <p>Brackenridge Works Equipment Hire specialise in the hire of heavy earthmoving, mining and construction machines with specialised attachments and tooling. Our array of machines and attachments is second to none, and we have one of the largest hire fleets available in South East Queensland. If its plant hire you require, then Brackenridge Works Resources, or BRW as the local's call us – should be the first call you make. Wet or dry hire, we provide excellent operators and quality machines across all makes and models to guarantee you maximum up time.</p>
</div>
<a class="btn abs" style="left:719px;top:1398px;width:229px;height:52px;font-size:12px">Discover More About Us</a>

<section class="stats">
  <div class="stat" style="left:86px">
    <svg width="62" height="66" viewBox="0 0 62 66" fill="none" stroke="#fff" stroke-width="1.4"><circle cx="31" cy="40" r="16"/><circle cx="31" cy="40" r="10"/><path d="M26 40l4 4 7-7"/><path d="M31 4l3 6 6 .8-4.5 4.3 1 6-5.5-3-5.5 3 1-6L22 10.8l6-.8z"/><path d="M12 14l2 3.5 3.8.5-2.8 2.7.7 3.8-3.7-2-3.6 2 .7-3.8L6 18l3.8-.5z"/><path d="M50 14l2 3.5 3.8.5-2.8 2.7.7 3.8-3.7-2-3.6 2 .7-3.8L44 18l3.8-.5z"/></svg>
    <div class="num">20+</div><div class="lbl">Years Of Experience</div>
  </div>
  <div class="stat" style="left:298px">
    <svg width="62" height="66" viewBox="0 0 62 66" fill="none" stroke="#fff" stroke-width="1.4"><circle cx="25" cy="22" r="10"/><circle cx="25" cy="22" r="4"/><circle cx="42" cy="30" r="7"/><circle cx="42" cy="30" r="2.5"/><path d="M8 52l10-6h12l8-4c3 0 3 3 1 4l-10 6h-8"/><path d="M8 58l6-2h16l18-10c2-1 4 1 2 3L32 60H8"/></svg>
    <div class="lbl only">Onsite Servicing</div>
  </div>
  <div class="stat" style="left:516px">
    <svg width="62" height="66" viewBox="0 0 62 66" fill="none" stroke="#fff" stroke-width="1.4"><path d="M6 14l16-4 18 4 16-4v42l-16 4-18-4-16 4z"/><path d="M22 10v42M40 14v42"/><path d="M12 30h10l6 6h12"/><circle cx="46" cy="24" r="4"/></svg>
    <div class="lbl only">One Of Qld's<br>argest Suppliers</div>
  </div>
  <div class="stat" style="left:730px">
    <svg width="72" height="66" viewBox="0 0 72 66" fill="none" stroke="#fff" stroke-width="1.4"><rect x="6" y="44" width="38" height="12" rx="6"/><circle cx="12" cy="50" r="3"/><circle cx="38" cy="50" r="3"/><path d="M10 44V30h18l4 14M14 30V20h10v10"/><path d="M32 36l14-22 14 8-4 6"/><path d="M56 28l6 24H50"/></svg>
    <div class="num">100+</div><div class="lbl">Machines In Fleet</div>
  </div>
  <div class="stat" style="left:921px">
    <svg width="62" height="66" viewBox="0 0 62 66" fill="none" stroke="#fff" stroke-width="1.4"><rect x="6" y="52" width="50" height="8"/><circle cx="14" cy="56" r="2"/><circle cx="31" cy="56" r="2"/><circle cx="48" cy="56" r="2"/><path d="M26 52V36l-6-12 8-16 10 4-6 12 4 8v20"/><rect x="40" y="40" width="8" height="12"/><rect x="12" y="40" width="8" height="12"/></svg>
    <div class="lbl only">Custom Machine<br>Attachments</div>
  </div>
</section>

<section class="plant">
  <div class="plant-deco"></div>
  <div class="abs center eyebrow" style="top:64px;color:#8a8a90">Plant Hire</div>
  <h2 class="abs center h2" style="top:84px;font-size:29px">Reliable plant hire spanning<br>Queensland and surrounds</h2>
  <div class="abs center" style="top:171px;font-size:10.5px;color:#333">We Have One of the Largest and Most Versatile Fleets in South East Queensland.</div>

  <svg class="abs" style="left:118px;top:220px" width="964" height="343" viewBox="0 0 964 343" role="img" aria-label="Fleet photos: orange excavator, yellow dump truck and line of scrapers on site">
    <defs>
      <linearGradient id="s1" x1="0" y1="0" x2="0" y2="1"><stop offset="0" stop-color="#4f8ed8"/><stop offset=".45" stop-color="#9db7cf"/><stop offset=".7" stop-color="#b69a78"/><stop offset="1" stop-color="#7c6a55"/></linearGradient>
      <linearGradient id="s3" x1="0" y1="0" x2="0" y2="1"><stop offset="0" stop-color="#2a54a8"/><stop offset=".5" stop-color="#c9a93a"/><stop offset="1" stop-color="#3d3a33"/></linearGradient>
      <linearGradient id="s4" x1="0" y1="0" x2="0" y2="1"><stop offset="0" stop-color="#4c86cf"/><stop offset=".5" stop-color="#a9b8c6"/><stop offset=".75" stop-color="#c79a5b"/><stop offset="1" stop-color="#a07e55"/></linearGradient>
      <linearGradient id="s2" x1="0" y1="0" x2="0" y2="1"><stop offset="0" stop-color="#3d4a98"/><stop offset="1" stop-color="#232a7a"/></linearGradient>
    </defs>
    <polygon points="16,0 252,0 236,343 0,343" fill="url(#s1)"/>
    <polygon points="252,0 490,0 474,343 236,343" fill="url(#s2)"/>
    <polygon points="490,0 726,0 710,343 474,343" fill="url(#s3)"/>
    <polygon points="726,0 964,0 948,343 710,343" fill="url(#s4)"/>
    <g stroke="#fff" stroke-width="4"><line x1="252" y1="0" x2="236" y2="343"/><line x1="490" y1="0" x2="474" y2="343"/><line x1="726" y1="0" x2="710" y2="343"/></g>
  </svg>
  <div class="abs" style="left:358px;top:386px;width:240px;text-align:center;color:#fff">
    <div style="font-size:14px;font-weight:500;font-style:italic">Dozers For Hire</div>
    <div style="font-size:10px;font-style:italic;line-height:17px;margin-top:10px;padding:0 26px">The most prolific brands of dozer manufacturers are Ridgeline &amp; Kovar – and we have both machine brands available for hire based on your preference.</div>
    <div style="font-size:12px;margin-top:10px">›</div>
  </div>
  <div class="arrow" style="left:53px"><svg width="12" height="12" viewBox="0 0 12 12"><path d="M8 2L4 6l4 4" stroke="#fff" stroke-width="1.6" fill="none"/></svg></div>
  <div class="arrow" style="left:1105px"><svg width="12" height="12" viewBox="0 0 12 12"><path d="M4 2l4 4-4 4" stroke="#fff" stroke-width="1.6" fill="none"/></svg></div>
</section>

<div class="partner" style="left:93px;width:84px;height:36px;top:2591px"></div>
<div class="partner" style="left:231px;width:77px"></div>
<div class="partner" style="left:360px;width:90px;height:24px;top:2597px"></div>
<div class="partner" style="left:495px;width:86px;height:30px;top:2594px;border-radius:15px"></div>
<div class="partner" style="left:630px;width:90px;height:40px;top:2589px"></div>
<div class="partner" style="left:766px;width:84px;height:50px;border-radius:50%"></div>
<div class="partner" style="left:898px;width:90px;height:32px;top:2593px"></div>
<div class="partner" style="left:1042px;width:74px;height:56px;top:2580px"></div>

<div class="abs contact-photo" role="img" aria-label="Yellow excavator with bucket on a dry site under a blue sky"></div>
<div class="contact-deco"></div>
<div class="abs" style="left:674px;top:2766px">
  <div class="eyebrow" style="color:#8a8a90;margin-bottom:10px">Contact Us</div>
  <h2 class="h2" style="font-size:29px;line-height:34px">Contact us today<br>for a free quote</h2>
</div>
<form class="form">
  <div class="title">Fill The Form Below:</div>
  <div class="field" style="margin-top:14px">Full Name</div>
  <div class="field">Phone Number</div>
  <div class="field">Email Address</div>
  <div class="field big">How We Can Help...</div>
  <div class="btn" style="margin-top:13px;width:178px;height:46px;box-shadow:none;font-size:12px;margin-left:2px">Submit Request</div>
</form>
<div class="abs strap">ALL TIME, ANYTIME, ANYWHERE ON TIME</div>
<div class="abs strap-sub">We do oversize and specialty vehicles servicing all of Queensland, NSW and other parts of Australia</div>
<a class="btn abs" style="left:763px;top:3365px;width:230px;height:60px;background:var(--accent);font-size:12px">Get Free Quotation</a>

<footer class="footer">
  <div class="abs" style="left:100px;top:3590px;width:162px;text-align:center">
    <div style="font-weight:700;font-size:44px;color:var(--navy);line-height:1;letter-spacing:2px">BRW</div>
    <div style="font-weight:600;font-size:10px;letter-spacing:4px;margin-top:4px">PLANT HIRE</div>
  </div>
  <div class="social" style="left:113px;background:var(--ink)"></div>
  <div class="social" style="left:146px"></div>
  <div class="social" style="left:179px"></div>
  <div class="social" style="left:212px"></div>

  <h4 class="abs" style="left:336px;top:3555px">Quick Links</h4>
  <ul class="abs flist" style="left:336px;top:3582px">
    <li>Home</li><li>About us</li><li>Machine Operator Jobs</li><li>Plant Hire</li><li>Attachments Hire</li><li>Policies</li><li>Grader Hire</li><li>Articulated Dump Trucks Hire</li><li>Dozer Hire</li>
  </ul>
  <ul class="abs flist" style="left:535px;top:3582px">
    <li>Excavator Diggers Hire</li><li>Attachments Hire</li><li>Backhoe Hire</li><li>Compactors Hire</li><li>Loader Hire</li><li>Skid Steer Hire</li><li>Water Cart Hire</li>
  </ul>

  <h4 class="abs" style="left:730px;top:3555px">Contact Us</h4>
  <div class="abs" style="left:730px;top:3584px;width:150px;font-size:10px;color:#66666c;line-height:18px">
    <div style="display:flex;gap:10px;align-items:center"><svg width="10" height="10" viewBox="0 0 24 24"><path fill="#232a7a" d="M6.6 10.8a15 15 0 006.6 6.6l2.2-2.2c.3-.3.7-.4 1-.2 1.1.4 2.3.6 3.6.6.6 0 1 .4 1 1V20c0 .6-.4 1-1 1A17 17 0 013 4c0-.6.4-1 1-1h3.5c.6 0 1 .4 1 1 0 1.3.2 2.5.6 3.6.1.3 0 .7-.2 1z"/></svg>1300 462 915</div>
    <div style="display:flex;gap:10px;align-items:center;margin-top:14px"><svg width="10" height="10" viewBox="0 0 24 24"><path fill="#232a7a" d="M2 5h20v14H2z"/><path d="M2 5l10 8 10-8" stroke="#fff" stroke-width="2" fill="none"/></svg><span style="text-decoration:underline;color:var(--accent)">hello@brwplant.com.au</span></div>
    <div style="display:flex;gap:10px;margin-top:14px"><svg width="10" height="12" viewBox="0 0 24 28"><path fill="#232a7a" d="M12 0a10 10 0 0110 10c0 7-10 18-10 18S2 17 2 10A10 10 0 0112 0zm0 6a4 4 0 100 8 4 4 0 000-8z"/></svg><span>14 Ironbark Rd,<br>Wattleby QLD 4391</span></div>
  </div>
  <div class="abs" style="left:893px;top:3553px;width:214px;height:172px;background:linear-gradient(135deg,#eef1f4,#dfe6ec 60%,#e9e4d4)" role="img" aria-label="Street map showing the depot location"></div>
</footer>

<div class="copybar">
  <span class="abs" style="left:93px;top:13px">Copyrights 2024. All Rights Reserved</span>
  <span class="abs" style="left:900px;top:13px">Privacy Policy</span>
  <span class="abs" style="left:985px;top:13px">|</span>
  <span class="abs" style="left:1011px;top:13px">Terms &amp; Conditions</span>
</div>

</body>
</html>
```